Modern, upmarket label design for food product

We need a label design for a food company producing nuts with sesame and honey. In fact, we would like the words "Cashews med sesam & honning" on the label (It's in Danish and means - Cashews with sesame & honey). It should be easy for the customer to quickly understand what it is.

It is a shelf product in the competitive food industry, which is why the design should wake the feeling of 'just wanting to grab the product down from the shelves'. So, the design should stand out and have an image of a cool, modern, hip product. This being said, I love a raw & handmade look.

The company is called Tyvo. Its origins are from the danish word Pilt that is a Danish slang for yummy. I have uploaded a photo of the package the products will be sold in.

Info & dimensions on bag in picture 1.
Dimensions: 6" x 9" | 15.2 cm x 22.3 cm
Capacity: 8 ounces | 250 grams (based on whole bean coffee)

Picture 2 is the same product, but has the possibility of attaching to a hanger on shelfs.

Picture 3 - I have also uploaded a photo of a product bag, where the hole is linear instead of a round hole. The designer chooses, which bag they will like to work with!

Please let me know if there are any questions!

Target Market(s)

Target market could really be any age, but the design needs to compel the target audience to pick it from the shelves. The package should signal a product you want to hold and have other people seeing you have it. The target audience is people who cares for what they buy, and typically doesn't want a low-end or budget product. They want the whole thing, meaning it has to taste good, look good etc. They are also the type of people who like to show off whatever products they buy by placing them in their houses for their guests to see. Or by uploading pictures of it on social medias.

Industry/Entity Type

It Company

Font styles to use
Other font styles liked:
• Not a must, but I like the 'Panton' script

Requirements
Must have
• My project must have the words 'Cashews med sesam & honning' on the label, so the customer will know within a second what they are looking at and buying.
Nice to have
• I am picturing the label with the words 'Cashews med sesam & honning' as a statement, again, emphasizing how the customer instantly should know what the product is. This being said, it should not be the only thing on the package and I love a raw & handmade look - which inspiration picture 5 is a great example of!
• I have uploaded photos of what I think looks good. With this said, I am not looking for a copy of those products, but see them as good inspiration. I have named the photos inspiration 1, 2, 3, 4 & 5.
• If needed, more text can be put on the label. For example 'vegan', 'laktosefri', Glutenfri', or 'Sund Snack' are great words for being used on the label.
Should not have
• The fonts on the label should not be too decorative. Personally I like an easy too read font.

```html
<!DOCTYPE html>
<html lang="da">
<head>
<meta charset="utf-8">
<title>Cashews med sesam &amp; honning – label</title>
<link rel="stylesheet" href="https://fonts.googleapis.com/css2?family=Oswald:wght@600;700&family=Nunito:wght@800&family=Roboto:wght@400;500&display=swap">
<style>
  :root {
    --canvas: #ffffff;
    --label-slate: #52768b;
    --label-sky: #a8cce6;
    --label-white: #ffffff;
    --ribbon-shade: #8fb6d2;
  }
  html, body {
    margin: 0;
    padding: 0;
    width: 1200px;
    height: 1005px;
    overflow: hidden;
    background: var(--canvas);
  }
  .canvas {
    position: relative;
    width: 1200px;
    height: 1005px;
  }
  .product-label {
    position: absolute;
    left: 240px;
    top: 142px;
    width: 720px;
    height: 720px;
  }
  .label-body { fill: var(--label-slate); }
  .headline {
    font-family: "Oswald", "Arial Narrow", sans-serif;
    font-weight: 700;
    fill: var(--label-sky);
  }
  .connector {
    font-family: "Roboto", Arial, sans-serif;
    font-weight: 500;
    fill: var(--label-white);
  }
  .ampersand {
    font-family: "Roboto", Arial, sans-serif;
    font-weight: 500;
    fill: var(--label-white);
  }
  .ribbon-band { fill: var(--label-sky); }
  .ribbon-tail { fill: var(--ribbon-shade); }
  .claims {
    font-family: "Nunito", Arial, sans-serif;
    font-weight: 800;
    fill: var(--label-slate);
  }
  .maker-line {
    font-family: "Roboto", Arial, sans-serif;
    font-weight: 400;
    fill: var(--label-sky);
  }
  .brand-name {
    font-family: "Roboto", Arial, sans-serif;
    font-weight: 500;
    fill: var(--label-white);
    letter-spacing: 1px;
  }
</style>
</head>
<body>
<main class="canvas">
  <svg class="product-label" viewBox="0 0 460 460" role="group" aria-label="Cashews med sesam og honning, vegan, laktosefri, glutenfri, et produckt fra Tyvo">
    <path class="label-body" d="M6 8 L40 4 L62 9 L95 3 L130 8 L160 4 L198 9 L230 3 L262 8 L296 4 L330 9 L360 3 L394 8 L426 4 L455 7
      L452 40 L458 72 L453 108 L457 142 L452 176 L458 210 L453 246 L457 280 L452 316 L458 350 L453 386 L457 420 L454 454
      L420 458 L390 452 L356 457 L322 452 L288 458 L254 453 L220 457 L186 452 L152 458 L118 453 L84 457 L50 452 L20 457 L4 453
      L8 420 L3 386 L8 350 L2 316 L7 280 L3 246 L8 210 L2 176 L7 142 L3 108 L8 72 L3 40 Z"/>

    <text class="headline" x="40" y="113" font-size="94" textLength="375" lengthAdjust="spacingAndGlyphs">CASHEWS</text>
    <text class="connector" transform="translate(80 246) rotate(-90)" font-size="28" textLength="60" lengthAdjust="spacingAndGlyphs">med</text>
    <text class="headline" x="90" y="245" font-size="86" textLength="258" lengthAdjust="spacingAndGlyphs">SESAM</text>
    <text class="ampersand" x="350" y="228" font-size="72">&amp;</text>
    <text class="headline" x="45" y="329" font-size="90" textLength="370" lengthAdjust="spacingAndGlyphs">HONNING</text>

    <g class="claims-ribbon">
      <path class="ribbon-tail" d="M4 368 L34 362 L36 392 L12 396 L22 382 Z"/>
      <path class="ribbon-tail" d="M456 368 L426 362 L424 392 L448 396 L438 382 Z"/>
      <path class="ribbon-band" d="M24 356 Q230 322 436 356 L432 386 Q230 354 28 386 Z"/>
      <path id="claims-curve" d="M40 377 Q230 343 420 377" fill="none"/>
      <text class="claims" font-size="21">
        <textPath href="#claims-curve" startOffset="50%" text-anchor="middle">vegan  laktosefri  glutenfri</textPath>
      </text>
    </g>

    <text class="maker-line" x="230" y="398" font-size="10" text-anchor="middle">et produckt fra</text>
    <text class="brand-name" x="230" y="424" font-size="17" text-anchor="middle">TYVO</text>
  </svg>
</main>
</body>
</html>
```